Summer Sale Graphics for Social Media

I want to create 11 social media graphics (new Instagram size 4:5 (1080 x 1350 pixels) focusing on our Summer Sale Graphics, using any of the pics attached. Use the attached pics, NO RANDOM STOCK PHOTOGRAPHY. For the color scheme of the graphics, they should all be complementary to the product colors in the photos.
You can add any of the photos attached but none are required. You can do some of the graphics in all text. I mainly need BOLD text that says one of the headlines (11 total) SEE ATTACHED WORD DOCUMENT for the headlines to use.

```html
<!DOCTYPE html>
<html lang="en">
<head>
<meta charset="utf-8">
<title>Summer Sale – Biggest Sale of the Year</title>
<link href="https://fonts.googleapis.com/css2?family=Montserrat:wght@800;900&display=swap" rel="stylesheet">
<style>
  :root {
    --brand-blue: #2f47a8;
    --white: #ffffff;
    --photo-wall: #b48a68;
    --photo-warm: #8f6a52;
    --photo-felt: #b8324f;
    --photo-green: #6f8a4a;
  }
  * { margin: 0; padding: 0; box-sizing: border-box; }
  html, body { width: 960px; height: 1200px; overflow: hidden; background: #ffffff; }
  .sale-post {
    position: relative;
    width: 960px;
    height: 1200px;
    overflow: hidden;
    font-family: "Montserrat", sans-serif;
    color: var(--white);
  }
  .hero-photo {
    position: absolute;
    inset: 0;
    background:
      radial-gradient(ellipse 260px 520px at 640px 640px, #7a5a48 0%, rgba(122,90,72,0) 70%),
      radial-gradient(ellipse 220px 400px at 900px 380px, var(--photo-green) 0%, rgba(111,138,74,0) 75%),
      linear-gradient(180deg, var(--photo-wall) 0%, var(--photo-warm) 45%, var(--photo-felt) 62%, #7a3050 78%, #4a3a70 100%);
  }
  .hero-overlay {
    position: absolute;
    inset: 0;
    background: linear-gradient(180deg,
      rgba(58,74,168,0) 45%,
      rgba(91,63,154,0.45) 65%,
      rgba(58,74,168,0.85) 85%,
      rgba(58,74,168,0.95) 100%);
  }
  .ring-decor {
    position: absolute;
    left: -120px;
    top: 330px;
    width: 400px;
    height: 400px;
  }
  .offer-tag {
    position: absolute;
    left: 46px;
    display: flex;
    align-items: center;
    background: var(--brand-blue);
    font-weight: 900;
    line-height: 1;
    white-space: nowrap;
  }
  .offer-tag--lead {
    top: 69px;
    width: 250px;
    height: 113px;
    font-size: 82px;
    letter-spacing: -3px;
    padding: 0 0 8px 8px;
  }
  .offer-tag--amount {
    top: 191px;
    width: 375px;
    height: 113px;
    font-size: 78px;
    letter-spacing: -1px;
    padding: 0 0 8px 18px;
  }
  .offer-tag__word {
    position: relative;
    display: inline-block;
    margin-left: 0.22em;
  }
  .offer-tag__arrow {
    position: absolute;
    left: 0;
    top: 100%;
    width: 100%;
    height: 20px;
    margin-top: 2px;
  }
  .headline {
    position: absolute;
    left: 0;
    right: 0;
    top: 822px;
    text-align: center;
    font-weight: 900;
    font-size: 71px;
    line-height: 57px;
    letter-spacing: -0.5px;
    text-transform: uppercase;
  }
  .rating-stars {
    position: absolute;
    left: 0;
    right: 0;
    top: 1064px;
    display: flex;
    justify-content: center;
    gap: 21px;
  }
  .rating-stars svg { width: 35px; height: 35px; fill: var(--white); }
</style>
</head>
<body>
  <main class="sale-post">
    <div class="hero-photo" role="img" aria-label="Smiling woman in a brown turtleneck holding three supplement bottles, standing by a red pool table in a bright lounge with plants"></div>
    <div class="hero-overlay"></div>

    <svg class="ring-decor" viewBox="0 0 400 400" fill="none" stroke="#ffffff" stroke-linecap="round">
      <path d="M200 18 A182 182 0 1 1 88 344" stroke-width="5"/>
      <path d="M120 60 A160 160 0 0 1 360 200" stroke-width="4"/>
      <path d="M360 232 A160 160 0 0 1 120 340" stroke-width="4"/>
      <path d="M140 90 A130 130 0 0 1 210 72" stroke-width="4"/>
      <path d="M330 210 A130 130 0 0 1 200 330" stroke-width="4"/>
    </svg>

    <div class="offer-tag offer-tag--lead">Up to</div>
    <div class="offer-tag offer-tag--amount">$15<span class="offer-tag__word">OFF<svg class="offer-tag__arrow" viewBox="0 0 170 20" preserveAspectRatio="none" fill="#ffffff"><rect x="0" y="0" width="170" height="4"/><polygon points="14,4 156,4 85,19"/></svg></span></div>

    <h1 class="headline">Summer’s here<br>and we’re having<br>the biggest<br>sale of the year</h1>

    <div class="rating-stars" aria-label="Five stars">
      <svg viewBox="0 0 24 24"><polygon points="12,1 15,9 23.5,9 16.5,14 19.2,22.5 12,17.3 4.8,22.5 7.5,14 0.5,9 9,9"/></svg>
      <svg viewBox="0 0 24 24"><polygon points="12,1 15,9 23.5,9 16.5,14 19.2,22.5 12,17.3 4.8,22.5 7.5,14 0.5,9 9,9"/></svg>
      <svg viewBox="0 0 24 24"><polygon points="12,1 15,9 23.5,9 16.5,14 19.2,22.5 12,17.3 4.8,22.5 7.5,14 0.5,9 9,9"/></svg>
      <svg viewBox="0 0 24 24"><polygon points="12,1 15,9 23.5,9 16.5,14 19.2,22.5 12,17.3 4.8,22.5 7.5,14 0.5,9 9,9"/></svg>
      <svg viewBox="0 0 24 24"><polygon points="12,1 15,9 23.5,9 16.5,14 19.2,22.5 12,17.3 4.8,22.5 7.5,14 0.5,9 9,9"/></svg>
    </div>
  </main>
</body>
</html>
```